Single-sided business card for restaurant bellwether with new logo made on this site

Business card options with new logo including restaurant name, address, phone number and website. This business card is single-sided only and will be presented at the hostess desk for clients to take. I would like to see options based on a cream card background, a white card background, a yellow card background and a burgundy colored background. It needs to be elegant and traditional.

Target Market(s)

local and international crowd

Industry/Entity Type

restaurant

Contact Information for Business Card

address, website and phone number

Font styles to use
Serif

Colors
EE7325
F08F49
F5BC92
FAE3D3
FDF4ED

Requirements
Must have
• new logo, address, phone number, website
Should not have
• more than three colors

```html
<!DOCTYPE html>
<html lang="es">
<head>
<meta charset="utf-8">
<title>Bellwether – Tarjetas de presentación</title>
<link rel="stylesheet" href="https://fonts.googleapis.com/css2?family=Cinzel:wght@500;600&display=swap">
<style>
  :root {
    --backdrop: #c9c9c9;
    --card: #ecebed;
    --ink: #2e1a1c;
    --gold: #e3a12b;
  }
  * { margin: 0; padding: 0; box-sizing: border-box; }
  html, body { width: 1200px; height: 1101px; overflow: hidden; }
  body {
    background: var(--backdrop);
    font-family: "Cinzel", "Times New Roman", serif;
    color: var(--ink);
    position: relative;
  }
  .business-card {
    position: absolute;
    top: 265px;
    width: 304px;
    height: 534px;
    background: var(--card);
    text-align: center;
  }
  .business-card--plain { left: 246px; }
  .business-card--framed { left: 639px; }
  .business-card--framed::before {
    content: "";
    position: absolute;
    inset: 20px 18px 18px 19px;
    border: 1.5px solid var(--gold);
  }
  .brand-mark {
    display: block;
    width: 93px;
    height: 93px;
    margin: 64px auto 0;
    background: var(--gold);
  }
  .brand-name {
    margin-top: 30px;
    font-size: 27px;
    font-weight: 600;
    letter-spacing: 3px;
    line-height: 32px;
  }
  .brand-since {
    display: flex;
    align-items: center;
    justify-content: center;
    gap: 8px;
    margin-top: 4px;
    font-size: 7px;
    font-weight: 500;
    letter-spacing: 0.5px;
  }
  .brand-since::before, .brand-since::after {
    content: "";
    width: 44px;
    height: 1px;
    background: var(--gold);
  }
  .card-details {
    margin-top: 42px;
    font-size: 14.5px;
    font-weight: 600;
    line-height: 21px;
  }
  .divider {
    width: 62px;
    height: 1px;
    margin: 16px auto 16px;
    background: var(--gold);
  }
  .website { font-size: 13.5px; letter-spacing: 0.3px; }
</style>
</head>
<body>
  <article class="business-card business-card--plain">
    <span class="brand-mark"></span>
    <h1 class="brand-name">BELLWETHER</h1>
    <p class="brand-since">Desde 1999</p>
    <div class="card-details">
      <p>Restaurant Bellwether</p>
      <div class="divider"></div>
      <p>Magnolia 418<br>Bahías de Costa Verde,<br>Oaxaca CP 70412</p>
      <div class="divider"></div>
      <p>Reservaciones<br>958-410-2276</p>
      <p class="website">WWW.BELLWETHER.COM.MX</p>
    </div>
  </article>

  <article class="business-card business-card--framed">
    <span class="brand-mark"></span>
    <h1 class="brand-name">BELLWETHER</h1>
    <p class="brand-since">Desde 1999</p>
    <div class="card-details">
      <p>Restaurant Bellwether</p>
      <div class="divider"></div>
      <p>Magnolia 418<br>Bahías de Costa Verde,<br>Oaxaca CP 70412</p>
      <div class="divider"></div>
      <p>Reservaciones<br>958-410-2276</p>
      <p class="website">WWW.BELLWETHER.COM.MX</p>
    </div>
  </article>
</body>
</html>
```